Vantoralis 'Private Prism' Book Cover Design project

I need to revise the book cover design I have for my coming book. The design I created through CraftHerd is great but the book has grown and changed so I'm looking for an alternative/option design. I can then choose later from the different options.

I need a book cover that represents the unique book I am creating.

Book Title:
Your True Spectrum

Subtitle: Walking Your Path and Not Your Tag

The book is targeting all readers with a special focus on same sex attracted readers. It should not have stereotypical images.

I am including a file of the book cover I have had designed. The back cover blurb, author info and author pic will remain the same. The colouring of the back cover and spine will, of course, change to match the colouring of the front cover.

The new title will be on the spine and the new title wording.

The front cover will be markedly different using the bold images and rainbow colours of the images found in the files I am uploading for you.

I am thinking of a large boldly coloured rainbow face with the title and subtitle ON the image. The image will be the whole cover. It will fill the cover as much as possible with the text added onto the pic.

The bold pictures I am including will give you the idea of what I'm looking for.

ANY of the images I've uploaded can be used as the actual front cover image OR the designer might have/find some suitable image to be used. The image is to be large and bold and fill the cover. Hopefully a positive energy.
It needs to be eye-catching and striking and bold and positive.

So...the book cover sample file I've provided can keep the back cover with completely new colouring. The front cover is completely new with new image, wording and energy.

It is to be a rainbow coloured face or figure for the cover image.

I hope that is clear enough for you. I'm very happy to discuss and clarify these ideas with the designer. Looking forward to another great CraftHerd experience.

Target Market(s)

Wide audience with special focus on Same Sex Attracted individuals

Font styles to use
Script
Other font styles liked:
• Some form of handwriting font to make the book title and text appear more personal....as if handwritten by me.

Requirements
Must have
• Boldness, Quirky, Rainbow Colour, Image to fill the cover, maybe dark cover contrasting background.
Nice to have
• A well balanced back cover especially in the area where the barcode will be placed.
Should not have
• No stereotypical images

```html
<!DOCTYPE html>
<html lang="en">
<head>
<meta charset="utf-8">
<title>Your True Spectrum – Cover Presentation</title>
<link rel="stylesheet" href="https://fonts.googleapis.com/css2?family=Damion&family=Kalam:wght@300;400&family=Amatic+SC:wght@400;700&family=Crimson+Text:ital@0;1&family=Montserrat:wght@400;700&display=swap">
<style>
  :root {
    --page: #ffffff;
    --panel: #eef0f0;
    --cover-dark: #1d1d1e;
    --band-dark: #222224;
    --ink: #ffffff;
    --ink-soft: #d9d9d9;
    --cyan: #3fb8e6;
    --orange: #c9681f;
    --stripe-1: #7fe3d8;
    --stripe-2: #b6d334;
    --stripe-3: #f04fc2;
    --stripe-4: #ef7a22;
    --stripe-5: #45b8ea;
    --box-line: #3a3a3c;
  }
  * { box-sizing: border-box; margin: 0; padding: 0; }
  html, body { width: 939px; height: 1200px; overflow: hidden; background: var(--page); }
  .sheet { position: relative; width: 939px; height: 1200px; }
  .sheet__panel { position: absolute; left: 0; top: 0; width: 534px; height: 635px; background: var(--panel); }

  .mount { position: absolute; overflow: hidden; }
  .mount--front { left: 68px; top: 49px; width: 321px; height: 478px; }
  .mount--back { left: 578px; top: 58px; width: 315px; height: 477px; }
  .mount--front .front { transform: scale(0.7985, 0.7875); transform-origin: 0 0; }
  .mount--back .back { transform: scale(0.7975, 0.786); transform-origin: 0 0; }

  .spread { position: absolute; left: 58px; top: 563px; width: 831px; height: 607px; background: var(--cover-dark); }
  .spread .back { position: absolute; left: 0; top: 0; }
  .spread .front { position: absolute; left: 429px; top: 0; }

  /* Front cover */
  .front { position: relative; width: 402px; height: 607px; background: var(--cover-dark); }
  .front__photo { position: absolute; left: 0; top: 0; width: 402px; height: 394px;
    background:
      radial-gradient(ellipse 30% 35% at 22% 30%, rgba(240,80,190,.55), transparent 70%),
      radial-gradient(ellipse 25% 25% at 40% 15%, rgba(70,180,230,.5), transparent 70%),
      radial-gradient(ellipse 30% 30% at 35% 75%, rgba(240,120,40,.45), transparent 70%),
      radial-gradient(ellipse 25% 30% at 15% 85%, rgba(170,60,220,.5), transparent 70%),
      linear-gradient(90deg, #2b1f2a 0%, #140f14 55%, #050505 100%); }
  .front__band { position: absolute; left: 0; top: 394px; width: 402px; height: 155px; background: var(--band-dark); text-align: center; color: var(--ink); }
  .front__strip { position: absolute; left: 0; top: 549px; width: 402px; height: 58px;
    background: linear-gradient(90deg, #c03fb0, #f26a2a 20%, #3a2a4a 40%, #d94fa8 60%, #5ab0e0 80%, #1a1a1a); }
  .front__title { position: absolute; left: 0; right: 0; top: 14px; font-family: "Damion", cursive; font-weight: 400; font-size: 50px; line-height: 1; }
  .front__subtitle { position: absolute; left: 0; right: 0; top: 78px; font-family: "Kalam", cursive; font-weight: 300; font-size: 18px; letter-spacing: 1.2px; }
  .front__author { position: absolute; left: 0; right: 0; top: 115px; font-family: "Kalam", cursive; font-weight: 300; font-size: 22px; letter-spacing: 2px; }

  /* Back cover */
  .back { position: relative; width: 395px; height: 607px; background: var(--cover-dark); color: var(--ink); text-align: center; }
  .stripes { position: absolute; left: 12px; right: 12px; height: 4px; display: flex; gap: 14px; }
  .stripes--top { top: 0; }
  .stripes--bottom { bottom: 0; }
  .stripes span { flex: 1; }
  .stripes span:nth-child(1) { background: var(--stripe-1); }
  .stripes span:nth-child(2) { background: var(--stripe-2); }
  .stripes span:nth-child(3) { background: var(--stripe-3); }
  .stripes span:nth-child(4) { background: var(--stripe-4); }
  .stripes span:nth-child(5) { background: var(--stripe-5); }
  .back__quote { position: absolute; left: 12px; right: 12px; top: 14px; height: 72px; overflow: hidden; font-family: "Amatic SC", cursive; font-weight: 700; font-size: 19px; line-height: 23px; }
  .back__headline { position: absolute; left: 0; right: 0; top: 96px; font-family: "Montserrat", sans-serif; font-weight: 700; font-size: 10.5px; color: var(--cyan); }
  .back__lead { position: absolute; left: 0; right: 0; top: 111px; font-family: "Crimson Text", serif; font-weight: 400; font-size: 12.5px; }
  .back__blurb { position: absolute; left: 22px; right: 22px; top: 140px; font-family: "Crimson Text", serif; font-size: 10.6px; line-height: 16px; color: var(--ink-soft); }
  .back__pull { position: absolute; left: 0; right: 0; top: 280px; height: 80px; padding: 10px 60px 0; background: linear-gradient(180deg, #b95b19, var(--orange) 20%, var(--orange) 80%, #b95b19); font-family: "Crimson Text", serif; font-style: italic; font-size: 10.6px; line-height: 15.5px; }
  .back__close { position: absolute; left: 30px; right: 30px; top: 372px; font-family: "Crimson Text", serif; font-size: 10.6px; line-height: 16px; color: var(--ink-soft); }
  .back__portrait { position: absolute; left: 20px; top: 445px; width: 72px; height: 72px; border-radius: 50%; background: linear-gradient(180deg, #5f8a4a 0%, #8e7d62 45%, #9b4da8 60%, #c07ab8 100%); }
  .back__bio { position: absolute; left: 126px; top: 435px; text-align: left; font-family: "Montserrat", sans-serif; font-size: 7.4px; line-height: 14.8px; color: var(--ink-soft); }
  .back__bio-name { font-weight: 700; font-size: 9.5px; color: var(--ink); }
  .slot { position: absolute; border: 1px solid var(--box-line); background: #141415; font-family: "Montserrat", sans-serif; font-size: 8.5px; color: var(--ink-soft); display: flex; align-items: center; justify-content: center; }
  .slot--publisher { left: 20px; top: 539px; width: 107px; height: 48px; }
  .slot--second { left: 132px; top: 539px; width: 105px; height: 48px; }
  .slot--isbn { left: 251px; top: 515px; width: 124px; height: 72px; align-items: flex-start; padding-top: 22px; }

  /* Spine */
  .spine { position: absolute; left: 395px; top: 0; width: 34px; height: 607px; background: var(--cover-dark); color: var(--ink); }
  .spine__title { position: absolute; left: 4px; top: 22px; writing-mode: vertical-rl; font-family: "Damion", cursive; font-size: 25px; line-height: 26px; }
  .spine__author { position: absolute; left: 7px; top: 466px; writing-mode: vertical-rl; font-family: "Kalam", cursive; font-weight: 300; font-size: 16px; letter-spacing: 1.5px; }
</style>
</head>
<body>
<main class="sheet">
  <div class="sheet__panel"></div>

  <!-- Front cover, standalone -->
  <section class="mount mount--front">
    <div class="front">
      <div class="front__photo" role="img" aria-label="Cover photograph: figure with face and hands covered in bold rainbow body paint on black"></div>
      <div class="front__band">
        <h1 class="front__title">Your True Spectrum</h1>
        <p class="front__subtitle">Walking Your Path and Not Your Tag</p>
        <p class="front__author">Liam Dorrance</p>
      </div>
      <div class="front__strip" role="img" aria-label="Continuation of the rainbow paint photograph"></div>
    </div>
  </section>

  <!-- Back cover, standalone -->
  <section class="mount mount--back">
    <div class="back">
      <div class="stripes stripes--top"><span></span><span></span><span></span><span></span><span></span></div>
      <p class="back__quote">"It's important to challenge our accepted beliefs and the stories we tell ourselves individually and as a community, if there is to be any sense of wholeness, happiness and future."</p>
      <p class="back__headline">YOUR RAINBOW IS MUCH MORE THAN THE FLAG YOU WAVE.</p>
      <p class="back__lead">It is the unique and individual YOU behind the layers, labels and stories</p>
      <p class="back__blurb">This first book by Liam Dorrance asks each of us to consider our accepted beliefs and personal stories as we explore the possible ways to LIVE OUR LIFE AND NOT A LABEL. Doing this requires some honest inner work and a journey that will need to be passionately personal and authentically individual. 'Your True Spectrum' reminds us that a beautiful, rainbow life is more than sexuality, personality or gender or having a camp, team or tribe to belong to. It is much more than any acronym, scene or lifestyle. It's 'an inside job', deeply heartfelt and courageously unique. Finding and living the YOU of YOU has boldness and power and magic in it.</p>
      <p class="back__pull">"Living a meaningful, happy existence is about being true to the whole, complex, integrated person that you are and being strong enough and aware enough and reflective enough to know yourself, love yourself and be yourself" Liam Dorrance</p>
      <p class="back__close">This simple and insightful book will help you explore ways to bravely and honestly know, love and be yourself no matter what the rest of the world might be doing or saying or expecting.</p>
      <div class="back__portrait" role="img" aria-label="Author portrait"></div>
      <div class="back__bio">
        <p class="back__bio-name">Liam Dorrance</p>
        <p>Personal Change coach and Educator</p>
        <p>VANTORALIS Coaching and wellness</p>
        <p>Advocate, Activist, Writer and Support For MEN</p>
        <p>WHO DATE MEN and their wholeness</p>
        <p>happiness and human Rights</p>
      </div>
      <div class="slot slot--publisher">Publisher Logo 1</div>
      <div class="slot slot--second">Another logo</div>
      <div class="slot slot--isbn">ISBN / Barcode</div>
      <div class="stripes stripes--bottom"><span></span><span></span><span></span><span></span><span></span></div>
    </div>
  </section>

  <!-- Full wrap: back, spine, front -->
  <section class="spread">
    <div class="back">
      <div class="stripes stripes--top"><span></span><span></span><span></span><span></span><span></span></div>
      <p class="back__quote">"It's important to challenge our accepted beliefs and the stories we tell ourselves individually and as a community, if there is to be any sense of wholeness, happiness and future."</p>
      <p class="back__headline">YOUR RAINBOW IS MUCH MORE THAN THE FLAG YOU WAVE.</p>
      <p class="back__lead">It is the unique and individual YOU behind the layers, labels and stories</p>
      <p class="back__blurb">This first book by Liam Dorrance asks each of us to consider our accepted beliefs and personal stories as we explore the possible ways to LIVE OUR LIFE AND NOT A LABEL. Doing this requires some honest inner work and a journey that will need to be passionately personal and authentically individual. 'Your True Spectrum' reminds us that a beautiful, rainbow life is more than sexuality, personality or gender or having a camp, team or tribe to belong to. It is much more than any acronym, scene or lifestyle. It's 'an inside job', deeply heartfelt and courageously unique. Finding and living the YOU of YOU has boldness and power and magic in it.</p>
      <p class="back__pull">"Living a meaningful, happy existence is about being true to the whole, complex, integrated person that you are and being strong enough and aware enough and reflective enough to know yourself, love yourself and be yourself" Liam Dorrance</p>
      <p class="back__close">This simple and insightful book will help you explore ways to bravely and honestly know, love and be yourself no matter what the rest of the world might be doing or saying or expecting.</p>
      <div class="back__portrait" role="img" aria-label="Author portrait"></div>
      <div class="back__bio">
        <p class="back__bio-name">Liam Dorrance</p>
        <p>Personal Change coach and Educator</p>
        <p>VANTORALIS Coaching and wellness</p>
        <p>Advocate, Activist, Writer and Support For MEN</p>
        <p>WHO DATE MEN and their wholeness</p>
        <p>happiness and human Rights</p>
      </div>
      <div class="slot slot--publisher">Publisher Logo 1</div>
      <div class="slot slot--second">Another logo</div>
      <div class="slot slot--isbn">ISBN / Barcode</div>
      <div class="stripes stripes--bottom"><span></span><span></span><span></span><span></span><span></span></div>
    </div>
    <div class="spine">
      <p class="spine__title">Your True Spectrum</p>
      <p class="spine__author">Liam Dorrance</p>
    </div>
    <div class="front">
      <div class="front__photo" role="img" aria-label="Cover photograph: figure with face and hands covered in bold rainbow body paint on black"></div>
      <div class="front__band">
        <h2 class="front__title">Your True Spectrum</h2>
        <p class="front__subtitle">Walking Your Path and Not Your Tag</p>
        <p class="front__author">Liam Dorrance</p>
      </div>
      <div class="front__strip" role="img" aria-label="Continuation of the rainbow paint photograph"></div>
    </div>
  </section>
</main>
</body>
</html>
```